Bref créative
Complete Stationery Project for KMT
KMT - Real Estate Agency and Education Centre
I need double sided standard sized Business Card [3.5" x 2"]
Fonts and tag lines remain same font. Other texts, we're open to ideas from designers
Simple
Hendra Wiratmo
Owner / Realtor
Wisma Cakra Baruna 11 Floor
Jl. Raya Pemuda Kav. 3-4
Pasir Melati - Kebon Sirih
Jakarta Pusat - 10390
hendrawira@mailbox-example.com
www.hendra-wiratmo-example.com
K98765432
We require 2 different designs for 2 different companies. One is a real estate agency, the other is an education centre which provides courses in real estate, sales, motivation and personal development.
For the real estate agency:
- Name of company is P.T. Kirana Maju Teguh
- logo used shall be without the tagline
- tagline "The Heart of Property" to be placed separately
- we would like to see designs with and without personal photo, as not all agents might be placing their photos.
- Photos should not be in a box
- Name and Cell number needs to be more prominent than other details
- Design should be clean and exudes a branding of professionalism, trustworthiness and respect
For the education centre:
- Name of company is P.T. Sinar Budaya Akademi
- designs will be without photo
- name and cell number need NOT be more prominent
- design should be clean and corporate that exudes a branding of professionalism, reliability and trust
We require designs for:
- Business cards
- Open Top DL Envelopes 110mm x 220mm (plain)
- Open End DL Envelopes 110mm x 220mm (with window)
- Letter head
- Fax Cover
- 2 pocket folder with business card slot
- Open end envelopes 9 ½” x 12 ½”
Colours schemes are important to us to avoid 'clashes' with 'fengshui".
Colours allowed:
- Grey
Colours to be avoided:
- Yellow(and all other earthy colours)
- Green
- Brown(and all other woody colours)
- Red
We are open to ideas, but it should include the logo with tagline
Business card for the agency should also have the words "Buy / Sell / Lease"

```html
<!DOCTYPE html>
<html lang="en">
<head>
<meta charset="utf-8">
<title>KMT Business Cards</title>
<link href="https://fonts.googleapis.com/css2?family=Arimo:ital,wght@0,400;0,700;1,400&display=swap" rel="stylesheet">
<style>
  :root {
    --bg: #e9ebee;
    --card: #ffffff;
    --card-edge: #f1f3f5;
    --brand: #1c6fae;
    --brand-deep: #0d4f8a;
    --brand-light: #5fb4e6;
    --ink: #3a3f45;
    --muted: #6b7178;
    --rule: #c9d3dc;
  }
  * { margin: 0; padding: 0; box-sizing: border-box; }
  html, body { width: 1200px; height: 842px; overflow: hidden; }
  body {
    background: var(--bg);
    font-family: "Arimo", Arial, sans-serif;
    position: relative;
  }
  .card {
    position: absolute;
    width: 480px;
    height: 274px;
    border-radius: 14px;
    overflow: hidden;
    box-shadow: 0 6px 18px rgba(0,0,0,0.18);
  }
  /* Front card with details */
  .card-front {
    left: 110px; top: 220px;
    background: linear-gradient(180deg, var(--card) 0%, var(--card-edge) 100%);
  }
  .front-logo {
    position: absolute; left: 0; top: 0; width: 230px; height: 210px;
    display: flex; flex-direction: column; align-items: center; justify-content: center; gap: 8px;
  }
  .brand-row { display: flex; align-items: center; gap: 10px; }
  .logo-dot {
    width: 22px; height: 22px; border-radius: 50%; background: var(--brand);
  }
  .logo-name {
    font-weight: 700; color: var(--brand); letter-spacing: 1px;
  }
  .front-logo .logo-name { font-size: 54px; line-height: 1; }
  .services {
    font-size: 10px; font-weight: 700; color: var(--brand-deep);
    letter-spacing: 2px;
  }
  .front-divider {
    position: absolute; left: 232px; top: 28px; width: 1px; height: 170px;
    background: var(--rule);
  }
  .contact {
    position: absolute; left: 246px; top: 26px; width: 228px;
    font-size: 8.6px; line-height: 1.42; color: var(--ink);
  }
  .contact-name { font-size: 16px; font-weight: 700; color: var(--brand-deep); line-height: 1.2; }
  .contact-role { font-size: 9px; color: var(--muted); margin-bottom: 8px; }
  .contact-block { margin-bottom: 8px; }
  .contact-cell { font-size: 12px; font-weight: 700; color: var(--brand-deep); line-height: 1.4; }
  .contact-web { font-weight: 700; color: var(--brand); font-size: 9px; }
  .front-band {
    position: absolute; left: 0; right: 0; top: 214px; height: 22px;
    background: linear-gradient(90deg, var(--brand-light) 0%, var(--brand) 100%);
    display: flex; align-items: center; padding-left: 30px;
  }
  .tagline { font-style: italic; letter-spacing: 1.5px; }
  .front-band .tagline { color: #ffffff; font-size: 11px; }
  .front-base {
    position: absolute; left: 0; right: 0; top: 236px; bottom: 0;
    background: var(--brand-deep);
  }
  /* Blue back card */
  .card-back-blue {
    left: 650px; top: 180px;
    background: radial-gradient(ellipse at 60% 40%, #2f8fd0 0%, #1a63a6 55%, #0c3f78 100%);
  }
  .back-mark {
    position: absolute; right: 56px; top: 140px; text-align: left;
  }
  .back-mark .brand-row { gap: 8px; }
  .back-mark .logo-name { font-size: 40px; }
  .back-mark .mark-rule { height: 1px; margin: 4px 0 3px; }
  .back-mark .tagline { font-size: 9px; display: block; text-align: right; }
  .card-back-blue .logo-name { color: #ffffff; }
  .card-back-blue .logo-dot { background: #ffffff; }
  .card-back-blue .mark-rule { background: rgba(255,255,255,0.7); }
  .card-back-blue .tagline { color: #ffffff; }
  /* White back card */
  .card-back-white {
    left: 370px; top: 520px;
    background: linear-gradient(180deg, var(--card) 0%, var(--card-edge) 100%);
  }
  .card-back-white .mark-rule { background: var(--brand); }
  .card-back-white .tagline { color: var(--brand-deep); }
</style>
</head>
<body>

  <section class="card card-front">
    <div class="front-logo">
      <div class="brand-row">
        <span class="logo-dot"></span>
        <span class="logo-name">KMT</span>
      </div>
      <div class="services">Buy / Sell / Lease</div>
    </div>
    <div class="front-divider"></div>
    <div class="contact">
      <div class="contact-name">Hendra Wiratmo</div>
      <div class="contact-role">Owner / Realtor</div>
      <div class="contact-block">
        Wisma Cakra Baruna 11 Floor<br>
        Jl. Raya Pemuda Kav. 3-4<br>
        Pasir Melati - Kebon Sirih<br>
        Jakarta Pusat - 10390
      </div>
      <div class="contact-block">
        <div class="contact-cell">Cell: +65 9012 7735</div>
        Phone: +62 2100 4417<br>
        Fax: +62 2100 4418<br>
        Email: hendrawira@mailbox-example.com
      </div>
      <div class="contact-web">www.hendra-wiratmo-example.com</div>
    </div>
    <div class="front-band"><span class="tagline">The Heart of Property</span></div>
    <div class="front-base"></div>
  </section>

  <section class="card card-back-blue">
    <div class="back-mark">
      <div class="brand-row">
        <span class="logo-dot"></span>
        <span class="logo-name">KMT</span>
      </div>
      <div class="mark-rule"></div>
      <span class="tagline">The Heart of Property</span>
    </div>
  </section>

  <section class="card card-back-white">
    <div class="back-mark">
      <div class="brand-row">
        <span class="logo-dot"></span>
        <span class="logo-name">KMT</span>
      </div>
      <div class="mark-rule"></div>
      <span class="tagline">The Heart of Property</span>
    </div>
  </section>

</body>
</html>
```